No Credit Score QT and ZMR

I'm looking for a banner to display on emails as well as facebook. The facebook banner would need to be square and the other size is 728 x 90. We are a mortgage company that does mostly Military home loans. We would like to start out with just this banner, then do about 20 others once we find the right designer. I need something simple but that stands out. Our company website is www.harborpeakfinancial.com. The text for this will be ( Ask about our "No Credit Score" program for ZMR and QT)

```html
<!DOCTYPE html>
<html lang="en">
<head>
<meta charset="utf-8">
<title>Harbor Peak Financial – No Credit Score Program</title>
<link rel="stylesheet" href="https://fonts.googleapis.com/css2?family=Oswald:wght@500&display=swap">
<style>
  :root {
    --navy: #222a73;
    --navy-deep: #1c2266;
    --red: #c9212f;
    --red-dark: #a8141f;
    --white: #ffffff;
    --ink: #1b1f4f;
    --camo-light: #b9b8ae;
    --camo-mid: #8e8f84;
    --sky: #cfe6f2;
    --flag-red: #c23a3f;
    --flag-blue: #2d3f86;
  }
  * { box-sizing: border-box; margin: 0; padding: 0; }
  html, body {
    width: 1200px;
    height: 1200px;
    overflow: hidden;
    background: var(--white);
  }
  .banner {
    position: relative;
    width: 1200px;
    height: 1200px;
    overflow: hidden;
    font-family: "Oswald", "Arial Narrow", sans-serif;
    font-weight: 500;
    text-transform: uppercase;
  }
  .hero-photo {
    position: absolute;
    inset: 0 0 232px 0;
    background:
      radial-gradient(ellipse 420px 300px at 230px 90px, rgba(45,63,134,0.55), transparent 70%),
      radial-gradient(ellipse 520px 260px at 200px 120px, rgba(194,58,63,0.45), transparent 75%),
      radial-gradient(ellipse 380px 500px at 960px 560px, rgba(240,240,236,0.85), transparent 70%),
      linear-gradient(180deg, transparent 70%, var(--sky) 100%),
      linear-gradient(135deg, var(--camo-light) 0%, var(--camo-mid) 55%, var(--camo-light) 100%);
  }
  .band {
    position: absolute;
    left: 0;
    display: flex;
    align-items: center;
    padding-left: 66px;
    color: var(--white);
    letter-spacing: 1px;
  }
  .band--intro {
    top: 310px;
    width: 506px;
    height: 106px;
    background: var(--red);
    clip-path: polygon(0 0, 100% 0, 94% 100%, 0 100%);
    font-size: 56px;
  }
  .band--program {
    top: 444px;
    width: 860px;
    height: 140px;
    background: var(--navy);
    clip-path: polygon(0 0, 100% 0, 95% 100%, 0 100%);
    font-size: 66px;
  }
  .band--loans {
    top: 604px;
    width: 482px;
    height: 120px;
    background: var(--white);
    clip-path: polygon(0 0, 100% 0, 94% 100%, 0 100%);
    color: var(--ink);
    font-size: 52px;
  }
  .cta {
    position: absolute;
    left: 70px;
    top: 770px;
    width: 394px;
    height: 134px;
    border-radius: 22px;
    background: linear-gradient(180deg, var(--red) 0%, var(--red-dark) 100%);
    color: var(--white);
    font-size: 66px;
    letter-spacing: 1px;
    display: flex;
    align-items: center;
    justify-content: center;
  }
  .footer {
    position: absolute;
    left: 0;
    bottom: 0;
    width: 1200px;
    height: 232px;
    background: var(--navy-deep);
    display: flex;
    align-items: center;
    justify-content: center;
    gap: 34px;
  }
  .brand-mark {
    width: 84px;
    height: 84px;
    border-radius: 50%;
    background: var(--white);
  }
  .brand-name {
    color: var(--white);
    font-size: 74px;
    letter-spacing: 4px;
  }
</style>
</head>
<body>
  <main class="banner">
    <div class="hero-photo" role="img" aria-label="American flag waving above a soldier in camouflage uniform holding a small model house in cupped hands"></div>

    <div class="band band--intro">Ask about our</div>
    <div class="band band--program">No credit score program</div>
    <div class="band band--loans">For ZMR and QT</div>

    <div class="cta">Ask now</div>

    <footer class="footer">
      <span class="brand-mark" aria-hidden="true"></span>
      <span class="brand-name">Harbor Peak Financial, LLC</span>
    </footer>
  </main>
</body>
</html>
```